Ebook Design for Halvora Biosciences (Health and Dietary Supplements)

Halvora Biosciences is an exciting new company in the area of health and wellness. Health requires a multi-dimensional, interdisciplinary approach that encompasses a complete lifestyle. Our company believes in whole-health that incorporates the entire body to ultimately help you live better and longer. We invest in products that boost metabolic functions, enhance natural performance, and support a healthy lifespan. We need a design for our research eBook on our products that sticks true to our brand identity. Please use the colors royal blue and yellow.

```html
<!DOCTYPE html>
<html lang="en">
<head>
<meta charset="utf-8">
<title>Health and Dietary Supplements — Halvora Biosciences</title>
<link rel="stylesheet" href="https://fonts.googleapis.com/css2?family=Tulpen+One&family=Passion+One:wght@700&family=Kaushan+Script&display=swap">
<style>
  :root {
    --gold: #f2b705;
    --gold-deep: #e0a300;
    --royal: #2a45b8;
    --royal-deep: #1c2f86;
    --sky: #5b8fe0;
    --rule: #3d4566;
    --paper: #ffffff;
  }
  html, body {
    margin: 0;
    padding: 0;
    width: 800px;
    height: 1200px;
    overflow: hidden;
    background: var(--paper);
  }
  .ebook-cover {
    position: relative;
    width: 800px;
    height: 1200px;
    background: var(--paper);
  }
  .cover-art {
    position: absolute;
    inset: 0;
    display: block;
  }
  .brand-name {
    font-family: "Tulpen One", sans-serif;
    fill: var(--gold-deep);
    stroke: var(--gold-deep);
    stroke-width: 1.6px;
    font-size: 84px;
  }
  .title-health, .title-dietary {
    font-family: "Passion One", sans-serif;
    font-weight: 700;
    fill: var(--royal);
    font-size: 104px;
  }
  .title-and {
    font-family: "Kaushan Script", cursive;
    fill: var(--gold-deep);
    font-size: 32px;
  }
  .title-supplements {
    font-family: "Passion One", sans-serif;
    font-weight: 700;
    fill: var(--gold);
    font-size: 118px;
  }
</style>
</head>
<body>
<main class="ebook-cover">
  <svg class="cover-art" width="800" height="1200" viewBox="0 0 800 1200" xmlns="http://www.w3.org/2000/svg">
    <defs>
      <linearGradient id="paint-tones" x1="0" y1="0" x2="0.3" y2="1">
        <stop offset="0" stop-color="#f7cf4a"/>
        <stop offset="0.3" stop-color="#f2b705"/>
        <stop offset="0.45" stop-color="#1c2f86"/>
        <stop offset="0.6" stop-color="#f0bd1e"/>
        <stop offset="0.75" stop-color="#2a45b8"/>
        <stop offset="1" stop-color="#3552cf"/>
      </linearGradient>
      <linearGradient id="paint-fade" x1="0" y1="0" x2="0" y2="1">
        <stop offset="0" stop-color="#ffffff" stop-opacity="1"/>
        <stop offset="1" stop-color="#ffffff" stop-opacity="0"/>
      </linearGradient>
    </defs>

    <text class="brand-name" x="38" y="92" textLength="726" lengthAdjust="spacing">HALVORA BIOSCIENCES</text>
    <rect class="header-rule" x="0" y="119" width="800" height="3" fill="var(--rule)"/>

    <g class="cover-title" transform="skewX(-10)">
      <text class="title-health" x="100" y="318" textLength="294" lengthAdjust="spacingAndGlyphs">HEALTH</text>
      <text class="title-and" x="398" y="298" textLength="70" lengthAdjust="spacingAndGlyphs">and</text>
      <text class="title-dietary" x="478" y="318" textLength="352" lengthAdjust="spacingAndGlyphs">DIETARY</text>
      <text class="title-supplements" x="108" y="430" textLength="732" lengthAdjust="spacingAndGlyphs">SUPPLEMENTS</text>
    </g>

    <g role="img" aria-label="Abstract poured paint in yellow, navy and royal blue with light blue glitter streaks flowing in waves">
      <rect x="0" y="480" width="800" height="720" fill="url(#paint-tones)"/>
      <rect x="0" y="476" width="800" height="110" fill="url(#paint-fade)"/>
    </g>
  </svg>
</main>
</body>
</html>
```